DL Flyer for garden consultants. I will supply text and logo

To design an eye catching but simple, uncluttered flyer for letter box distribution. The text and logo are provided.

```html
<!DOCTYPE html>
<html lang="en">
<head>
<meta charset="utf-8">
<title>Fernleigh Garden Consultants – DL Flyer</title>
<link rel="stylesheet" href="https://fonts.googleapis.com/css2?family=Nunito:ital,wght@1,800;1,900&family=Open+Sans:wght@400;600;700&display=swap">
<style>
  :root {
    --green-deep: #1d6b2c;
    --green-mid: #2f8f32;
    --green-bright: #4aa82c;
    --lime: #c8e62a;
    --lime-soft: #a6d23a;
    --footer: #17552a;
    --white: #ffffff;
    --page: #f2f2f2;
    --band-light: #f6f7f2;
  }
  * { box-sizing: border-box; margin: 0; padding: 0; }
  html, body { width: 1044px; height: 1200px; overflow: hidden; }
  body {
    background: var(--page);
    font-family: "Open Sans", sans-serif;
    position: relative;
  }
  .panel {
    position: absolute;
    top: 108px;
    width: 470px;
    height: 984px;
    overflow: hidden;
    background: linear-gradient(160deg, var(--green-bright) 0%, var(--green-mid) 45%, var(--green-deep) 100%);
    box-shadow: 0 4px 14px rgba(0,0,0,0.18);
  }
  .panel--front { left: 36px; }
  .panel--back { left: 538px; }

  .headline {
    position: absolute;
    top: 30px; left: 0; width: 100%;
    text-align: center;
    font-family: "Nunito", sans-serif;
    font-style: italic;
    font-weight: 900;
    line-height: 1.02;
  }
  .headline__small { display: block; color: var(--white); font-size: 34px; font-weight: 800; }
  .headline__big { display: block; color: var(--lime); font-size: 64px; letter-spacing: 1px; }

  .thought {
    position: absolute;
    border: 7px solid var(--lime);
    border-radius: 42% 48% 40% 46% / 48% 42% 50% 44%;
  }
  .thought--front {
    left: 182px; top: 258px; width: 272px; height: 176px;
    background: linear-gradient(180deg, #8d9a84 0%, #9a9a5c 50%, #b3a46a 100%);
  }
  .thought--back {
    left: 74px; top: 780px; width: 262px; height: 170px;
    background: linear-gradient(180deg, #3f5a34 0%, #8c4b4a 40%, #7fa046 75%, #5e8d2e 100%);
  }
  .thought-dot {
    position: absolute; border-radius: 50%;
    border: 3px solid var(--lime); background: var(--green-mid);
  }

  .hill { position: absolute; display: block; }

  .portrait {
    position: absolute;
    left: 22px; top: 340px; width: 280px; height: 412px;
    border-radius: 120px 120px 0 0;
    background: linear-gradient(180deg, #c2543a 0%, #e8b89a 35%, #f4f4f2 60%, #e8e8e6 100%);
  }

  .front-band {
    position: absolute; left: 0; top: 752px; width: 100%; height: 162px;
    background: linear-gradient(180deg, var(--white), var(--band-light));
    text-align: center;
  }
  .front-band__hmm {
    font-family: "Nunito", sans-serif; font-style: italic; font-weight: 900;
    color: var(--green-deep); font-size: 44px; margin-top: 6px; letter-spacing: 1px;
  }
  .brand {
    display: inline-flex; align-items: center; gap: 12px;
    font-family: "Open Sans", sans-serif; font-weight: 600;
    color: var(--green-mid);
  }
  .brand__dot { width: 22px; height: 22px; border-radius: 50%; background: var(--green-bright); }
  .brand__name { font-size: 30px; letter-spacing: 1px; line-height: 1.05; text-align: left; }
  .brand__name small { display: block; font-size: 13px; letter-spacing: 3px; }
  .front-band .brand { margin-top: 10px; }

  .footer {
    position: absolute; left: 0; bottom: 0; width: 100%; height: 70px;
    background: var(--footer);
    color: var(--white);
    font-size: 22px; font-weight: 600;
    display: flex; align-items: center; justify-content: center;
  }

  .back-brand { position: absolute; top: 64px; left: 0; width: 100%; text-align: center; }
  .back-brand .brand { color: var(--lime); }
  .back-brand .brand__dot { background: var(--lime); }

  .help {
    position: absolute; top: 168px; left: 0; width: 100%; text-align: center;
    font-family: "Nunito", sans-serif; font-style: italic; font-weight: 900;
    color: var(--lime); font-size: 40px; letter-spacing: 1px;
  }

  .services { position: absolute; top: 238px; left: 28px; right: 22px; list-style: none; }
  .service { display: flex; gap: 14px; margin-bottom: 34px; }
  .service__bullet {
    flex: none; width: 34px; height: 34px; margin-top: 8px;
    border-radius: 50%; background: var(--lime-soft);
  }
  .service__title { color: var(--white); font-weight: 600; font-size: 25px; line-height: 1.2; }
  .service__note { color: var(--lime); font-size: 17px; font-weight: 600; line-height: 1.25; margin-top: 4px; }

  .cta-band {
    position: absolute; left: 0; top: 858px; width: 100%; height: 56px;
    background: var(--lime-soft);
    text-align: center;
    font-family: "Nunito", sans-serif; font-style: italic; font-weight: 900;
    color: var(--green-deep); font-size: 36px; line-height: 56px;
  }
</style>
</head>
<body>

  <section class="panel panel--front">
    <h1 class="headline">
      <span class="headline__small">Have you been</span>
      <span class="headline__big">THINKING</span>
      <span class="headline__small">about your</span>
      <span class="headline__big">Garden?</span>
    </h1>

    <svg class="hill" style="left:0;top:470px" width="470" height="290" viewBox="0 0 470 290" aria-hidden="true">
      <path d="M180 290 C230 150 330 70 470 40 L470 290 Z" fill="#8cc63f"/>
      <path d="M260 290 C300 220 380 180 470 170 L470 290 Z" fill="#3b9a36"/>
    </svg>

    <div class="thought thought--front" role="img" aria-label="Photo of an overgrown, untidy garden bed"></div>
    <div class="portrait" role="img" aria-label="Photo of a red-haired woman resting her chin on her hand, thinking"></div>

    <div class="front-band">
      <p class="front-band__hmm">Hmm........</p>
      <div class="brand">
        <span class="brand__dot"></span>
        <span class="brand__name">FERNLEIGH<small>GARDEN CONSULTANTS</small></span>
      </div>
    </div>
    <div class="footer">www.fernleighgardens.com.au</div>
  </section>

  <section class="panel panel--back">
    <div class="back-brand">
      <div class="brand">
        <span class="brand__dot"></span>
        <span class="brand__name">FERNLEIGH<small>GARDEN CONSULTANTS</small></span>
      </div>
    </div>

    <p class="help">........WE CAN HELP.</p>

    <ul class="services">
      <li class="service">
        <span class="service__bullet"></span>
        <div>
          <h2 class="service__title">Garden Assessment Consultation and Report</h2>
          <p class="service__note">...... information vital to ensuring your dream becomes reality!</p>
        </div>
      </li>
      <li class="service">
        <span class="service__bullet"></span>
        <div>
          <h2 class="service__title">Pre Sale Consultation and Report</h2>
          <p class="service__note">..... maximise your sale dollar!</p>
        </div>
      </li>
      <li class="service">
        <span class="service__bullet"></span>
        <div>
          <h2 class="service__title">Develop a Plant Portfolio</h2>
          <p class="service__note">..... successfully navigate the plant maze!</p>
        </div>
      </li>
    </ul>

    <svg class="hill" style="left:0;top:640px" width="470" height="220" viewBox="0 0 470 220" aria-hidden="true">
      <path d="M290 220 C320 120 390 50 470 20 L470 220 Z" fill="#8cc63f"/>
      <path d="M330 220 C360 170 410 140 470 130 L470 220 Z" fill="#3b9a36"/>
    </svg>

    <div class="thought thought--back" role="img" aria-label="Photo of a lush, flowering garden with a sprinkler watering the lawn"></div>
    <span class="thought-dot" style="left:218px;top:950px;width:16px;height:16px"></span>
    <span class="thought-dot" style="left:236px;top:966px;width:10px;height:10px"></span>

    <div class="cta-band">Check us out at</div>
    <div class="footer">www.fernleighgardens.com.au</div>
  </section>

</body>
</html>
```